Tallora Dinner, Dessert and Drinks Menu

We need to redesign our Dinner, Desserts, and Drinks Menus.
I have attached all three menus as pdfs. I have chosen the higher payment option because its a few pages and have removed the refund option
Tallora is the most popular Lebanese Restaurant in Melbourne and is a combination of Great Quality Traditional Food and a clean warm ambiance.
Updates
The main part of the menu is the Banquets Section. We want to push our Banquets.
The main focus of the drinks is Lebanese Wines, Lebanese Beer, Lebanese Drinks. Anything Traditional
For the Coffee Menu,
We will be Adding a Chai Latte, More Flavoured Loose Leaf Teas and Removing the Stick Tea. We will also be adding 4 coffee flavour shots to our menu.
Restaurant

```html
<!DOCTYPE html>
<html lang="en">
<head>
<meta charset="utf-8">
<title>Tallora – Platters, Sides, Kids and Banquets</title>
<link rel="stylesheet" href="https://fonts.googleapis.com/css2?family=Antonio:wght@200;300&family=Arimo:ital,wght@0,400;0,700;1,400;1,700&family=Kalam&display=swap">
<style>
:root{
  --backdrop:#ece6dc;
  --paper:#fbfaf3;
  --olive:#8fa24b;
  --olive-dark:#6f8236;
  --lime:#c8d85e;
  --heading-ink:#3b3a22;
  --cream-ink:#f6f3df;
  --orange:#e27b2c;
  --green-note:#7b9a2b;
  --ink:#1f1f1f;
  --muted:#3c3c3c;
  --band:#7d9a3a;
}
*{box-sizing:border-box;margin:0;padding:0}
html,body{width:1200px;height:920px;overflow:hidden}
body{background:var(--backdrop);position:relative;font-family:"Arimo",sans-serif;color:var(--ink)}
.page{position:absolute;top:92px;height:828px;background:var(--paper)}
.page--left{left:33px;width:567px}
.page--right{left:600px;width:568px}
.pattern-band{position:absolute;left:0;bottom:0;height:52px;width:100%;
  background:linear-gradient(180deg,#8aa843,var(--band))}

.banner{position:absolute;height:57px;display:flex;align-items:center;padding:0 20px;white-space:nowrap;
  font-family:"Antonio",sans-serif;font-weight:200;font-size:48px;letter-spacing:1px;line-height:1;
  clip-path:polygon(10px 0,calc(100% - 10px) 0,calc(100% - 10px) 6px,100% 6px,100% calc(100% - 6px),calc(100% - 10px) calc(100% - 6px),calc(100% - 10px) 100%,10px 100%,10px calc(100% - 6px),0 calc(100% - 6px),0 6px,10px 6px)}
.banner--olive{background:var(--olive);color:var(--cream-ink)}
.banner--lime{background:var(--lime);color:var(--heading-ink)}

.menu-list{position:absolute;list-style:none}
.item{margin-bottom:5px}
.item__row{display:flex;align-items:baseline;font-weight:700;font-size:12.5px;line-height:14px;color:var(--ink);white-space:nowrap}
.item__dots{flex:1;border-bottom:1.5px dotted #777;margin:0 2px 3px}
.item__desc{font-size:9px;line-height:1.15;color:var(--muted)}
.item--feature{position:absolute;left:19px;top:145px;width:253px;padding:4px 12px 4px 19px;
  border:2px solid var(--orange);background:#fff8e9;box-shadow:0 0 0 2px #f5d7b3 inset}
.veg-mark{position:absolute;left:-14px;font-weight:700;color:var(--olive-dark);font-size:12px}

.polaroid{position:absolute;background:#fff;padding:8px 8px 0;box-shadow:1px 2px 6px rgba(0,0,0,.35)}
.polaroid__photo{display:block;width:100%}
.polaroid__caption{font-family:"Kalam",cursive;font-size:13px;color:#555;text-align:center;padding:6px 0 4px}

.footnote{position:absolute;left:26px;top:752px;font-weight:700;font-size:6.6px;color:var(--ink);white-space:nowrap}

.brand{position:absolute;left:438px;top:36px;width:112px;height:36px;display:flex;align-items:center;justify-content:center;
  font-family:"Arimo",sans-serif;font-weight:700;font-size:22px;color:var(--heading-ink)}
.intro{position:absolute;left:27px;top:98px;width:240px}
.intro__title{font-style:italic;font-size:14px;color:var(--orange);margin-bottom:3px;white-space:nowrap}
.intro p{font-weight:700;font-size:7.8px;line-height:1.3;margin-bottom:3px}

.banquet{position:absolute;left:27px;width:240px}
.banquet__name{font-family:"Antonio",sans-serif;font-weight:200;font-size:24px;color:var(--orange);line-height:1;letter-spacing:.5px;white-space:nowrap}
.banquet__price,.banquet__group{font-weight:700;font-size:11.5px;color:var(--ink);white-space:nowrap}
.banquet__fill{flex:1;border-bottom:1.5px dotted #777;margin:0 3px 3px;min-width:6px}
.banquet__row{display:flex;align-items:baseline;width:100%}
.banquet__desc{font-size:9.6px;line-height:1.22;color:var(--ink)}
.banquet__note{color:var(--green-note);font-weight:700}
.veg-notice{position:absolute;left:27px;top:717px;width:238px;padding:4px 6px;border:2px solid var(--orange);
  background:#fdf0df;text-align:center;font-weight:700;font-size:9.4px;line-height:1.2;color:var(--heading-ink)}
.feature-photo{position:absolute;left:305px;top:98px;width:245px;height:658px;
  background:linear-gradient(170deg,#6b5a4a 0%,#b08656 30%,#d9b07a 55%,#c99548 75%,#b2704a 100%)}
</style>
</head>
<body>

<section class="page page--left">
  <h2 class="banner banner--olive" style="left:24px;top:26px;min-width:515px">TALLORA PLATTERS TO SHARE</h2>

  <ul class="menu-list" style="left:39px;top:98px;width:226px">
    <li class="item"><div class="item__row">Shish Platter<span class="item__dots"></span>$45.95</div>
      <p class="item__desc">2 lahem mishwee, 2 shish tawook, 2 shish kafta chargrilled and served with rice and salad.</p></li>
  </ul>
  <div class="item item--feature"><div class="item__row">Mixed Platter<span class="item__dots"></span>$46.95</div>
    <p class="item__desc">1 lahem mishwee, 1shish tawook, 1 shish kafta, 1 chicken kafta, 2 chicken wings, and 2 Lamb Chops, served with chips, rice, and salad.</p></div>
  <ul class="menu-list" style="left:39px;top:205px;width:226px">
    <li class="item" style="position:relative;margin-bottom:8px"><span class="veg-mark">V</span><div class="item__row">Vegetarian Platter<span class="item__dots"></span>$39.95</div>
      <p class="item__desc">Hummous, baba ghannouj, tabouli, warak areesh, falafel, borghul bid feen, and fatayer. Served with rice.</p></li>
    <li class="item"><div class="item__row">Family Platter<span class="item__dots"></span>$84.95</div>
      <p class="item__desc">3 lahem mishwee, 3 shish tawook, 3 shish kafta, 4 chicken wings, 4 falafel, served with hummous, hot chips, rice and house salad.</p></li>
  </ul>

  <figure class="polaroid" style="left:300px;top:102px;width:222px;transform:rotate(5deg)">
    <div class="polaroid__photo" role="img" aria-label="Photo of a shared platter with falafel, dips and bread" style="height:150px;background:radial-gradient(circle at 45% 45%,#a8733b,#c9b08a 55%,#7d7258)"></div>
    <figcaption class="polaroid__caption">Delicious Platter Combination?</figcaption>
  </figure>

  <h2 class="banner banner--lime" style="left:24px;top:311px;min-width:413px">TALLORA SOUPS &amp; SIDES</h2>
  <ul class="menu-list" style="left:39px;top:380px;width:226px">
    <li class="item"><div class="item__row">Chicken and Rice Soup<span class="item__dots"></span>$7</div></li>
    <li class="item"><div class="item__row">Crispy Herb Pita Chips<span class="item__dots"></span>$4</div><p class="item__desc">Great for Dipping!</p></li>
    <li class="item"><div class="item__row">Bowl of Hot Chips<span class="item__dots"></span>$6.50</div></li>
    <li class="item"><div class="item__row">Toum<span class="item__dots"></span>$4</div><p class="item__desc">Traditional Lebanese garlic sauce, great for dipping.</p></li>
    <li class="item"><div class="item__row">Kabeese<span class="item__dots"></span>$4</div><p class="item__desc">A delicious assortment of Lebanese pickles and olives.</p></li>
    <li class="item"><div class="item__row">Bowl of rice<span class="item__dots"></span>$6</div></li>
    <li class="item"><div class="item__row">House Salad<span class="item__dots"></span>$6</div></li>
  </ul>
  <figure class="polaroid" style="left:302px;top:374px;width:216px">
    <div class="polaroid__photo" role="img" aria-label="Photo of tabouli salad topped with tomato on a plate" style="height:130px;background:radial-gradient(circle at 50% 50%,#c0392b 0,#6f8a2a 30%,#4c5a24 60%,#2e2c22 100%)"></div>
    <figcaption class="polaroid__caption">Dish Description Here, Please</figcaption>
  </figure>

  <h2 class="banner banner--olive" style="left:24px;top:560px;min-width:241px">KIDS MENU</h2>
  <ul class="menu-list" style="left:39px;top:632px;width:226px">
    <li class="item"><div class="item__row">Chicken Nugget and Chips<span class="item__dots"></span>$9</div></li>
    <li class="item"><div class="item__row">Fish Fingers and Chips<span class="item__dots"></span>$9</div></li>
    <li class="item"><div class="item__row">Chicken Wings and Chips<span class="item__dots"></span>$9</div></li>
    <li class="item"><div class="item__row">Mini Pizzas and Chips<span class="item__dots"></span>$9</div></li>
    <li class="item"><div class="item__row">Bowl of Vanilla Ice Cream<span class="item__dots"></span>$4</div><div class="item__row">with Topping</div></li>
  </ul>
  <figure class="polaroid" style="left:304px;top:562px;width:214px;transform:rotate(4deg)">
    <div class="polaroid__photo" role="img" aria-label="Photo of a plate of colourful dips with bread" style="height:138px;background:radial-gradient(circle at 50% 50%,#e6d9b8 0,#c58a4a 35%,#9b3a4e 60%,#5a3a66 100%)"></div>
    <figcaption class="polaroid__caption">Dish Description Here, Please</figcaption>
  </figure>

  <p class="footnote">Please note, a 2% credit card surcharge will apply to all credit card transactions (including where you select the 'credit' option when paying by debit card).</p>
  <div class="pattern-band" role="img" aria-label="Green leaf pattern border"></div>
</section>

<section class="page page--right">
  <h2 class="banner banner--lime" style="left:27px;top:26px;min-width:391px">TALLORA BANQUETS</h2>
  <div class="brand">TALLORA</div>

  <div class="intro">
    <h3 class="intro__title">A Traditional Lebanese Experience</h3>
    <p>A banquet is a terrific way to share and sample an extensive range of the most popular Lebanese dishes. We serve a wide selection of mouth watering entrées and main courses followed by dessert and your choice of Lebanese coffee or Lebanese Loose Leaf tea.</p>
    <p>Only $2.00 extra if you prefer other coffees or teas from our menu (min. 2 people per table)</p>
  </div>

  <article class="banquet" style="top:190px">
    <div class="banquet__row"><span class="banquet__name">TALLORA BANQUET</span><span class="banquet__fill"></span><span class="banquet__price">$36.95 per person</span></div>
    <div class="banquet__row"><span class="banquet__group">Groups of 8 or More</span><span class="banquet__fill"></span><span class="banquet__group">$34.95 per person</span></div>
    <p class="banquet__desc">7 mouthwatering entrees plus a main course of a skewer each of our delicious Shish Kafta and Shish Tawook served with house salad and rice.</p>
  </article>
  <article class="banquet" style="top:269px">
    <div class="banquet__row"><span class="banquet__name">CEDAR BANQUET</span><span class="banquet__fill"></span><span class="banquet__price">$47.95 per person</span></div>
    <div class="banquet__row"><span class="banquet__group">Groups of 8 or More</span><span class="banquet__fill"></span><span class="banquet__group">$44.95 per person</span></div>
    <p class="banquet__desc">10 delicious dips and entrees to start with followed by a wonderful selection of mains. <span class="banquet__note">Our chefs change the entrees and mains monthly and include entrees that are especially made for the banquets.</span></p>
  </article>
  <article class="banquet" style="top:362px">
    <div class="banquet__name">BANQUET WITH SEAFOOD</div>
    <div class="banquet__row"><span class="banquet__fill"></span><span class="banquet__price">$52.95 per person</span></div>
    <div class="banquet__row"><span class="banquet__group">Groups of 8 or More</span><span class="banquet__fill"></span><span class="banquet__group">$49.95 per person</span></div>
    <p class="banquet__desc">Similar to the Cedar Banquet but served with Calamari, and spicy prawns plus samke harra as the main and one skewer of lamb or chicken.</p>
  </article>
  <article class="banquet" style="top:456px">
    <div class="banquet__row"><span class="banquet__name">ROYAL BANQUET</span><span class="banquet__fill"></span><span class="banquet__price">$62.95 per person</span></div>
    <div class="banquet__row"><span class="banquet__group">Groups of 8 or More</span><span class="banquet__fill"></span><span class="banquet__group">$59.95 per person</span></div>
    <p class="banquet__desc">A feast fit for a king! 16 table filling dips and entrees to start with followed by a wonderful selection of mains that will make everyone feel like royalty!</p>
  </article>
  <article class="banquet" style="top:537px">
    <div class="banquet__name">SEAFOOD ROYAL BANQUET</div>
    <div class="banquet__row"><span class="banquet__fill"></span><span class="banquet__price">$69.95 per person</span></div>
    <div class="banquet__row"><span class="banquet__group">Groups of 8 or More</span><span class="banquet__fill"></span><span class="banquet__group">$64.95 per person</span></div>
    <p class="banquet__desc">Similar to the Royal Banquet but served with Calamari, Tallora Prawns and Spicy Prawns plus Samke Harra as the main with a selection of other mains.</p>
  </article>
  <article class="banquet" style="top:633px">
    <div class="banquet__name">CHILDRENS BANQUET</div>
    <div class="banquet__row"><span class="banquet__group">Up to 12 years old</span><span class="banquet__fill"></span><span class="banquet__group">$19.95 per person</span></div>
    <p class="banquet__desc">Dip, salad, sambousik, and chicken wings followed by a choice of fish fingers and chips or Nuggets and chips. Yummy Ice cream for dessert.</p>
  </article>

  <p class="veg-notice">VEGETARIAN OPTIONS AVAILABLE FOR ALL BANQUETS. WE CAN ALSO ACCOMMODATE MOST DIETARY REQUIREMENTS.</p>

  <div class="feature-photo" role="img" aria-label="Photo of a banquet table with skewers, falafel and hummous bowls"></div>
  <div class="pattern-band" role="img" aria-label="Green leaf pattern border"></div>
</section>

</body>
</html>
```